Briar Hollow Family Law magazine ad

I need an ad that will run in Tidewell Homes Magazine here in NC. The ad will be a 1/2 page ad, (7.25X4.875). Resolution is 300 dpi or higher.

We are a family law firm (divorce) and we want to high light child custody issues. I would like the ad copy to include our logo (which you can find on our website www.briarhollowfamilylaw.com) and I can send a high res one if you are chosen. Ad MUST include our address and phone number by state law.

Ad copy will be something about protecting children (something brief) like "Protect what you love" or something like that. I will pick quick as I have to turn it in on Wednesday. You will need to be able to email the final product to graphics@tidewellhomesmag.com and me too.

Target Market(s)

Married couples with kids (primarily men) ages 35-50

Industry/Entity Type

Legal

Colors
85cae6
cadf82
fbee3f
fbf289
33a6d7
33b8a4
add136

Requirements
Must have
• website, logo, address, and phone number
Nice to have
• creative and heart provoking (I want the image to make me want to act)
Should not have
• Don't be boring or give me some stock photo I have seen in a million divorce ads.

```html
<!DOCTYPE html>
<html lang="en">
<head>
<meta charset="utf-8">
<title>Briar Hollow Family Law – Magazine Ad</title>
<link rel="stylesheet" href="https://fonts.googleapis.com/css2?family=Nunito:wght@400;800&display=swap">
<style>
  :root {
    --page-bg: #dcdcdc;
    --card-white: #ffffff;
    --lime: #add136;
    --teal: #33b8a4;
    --brand-blue: #2a78b5;
    --ink: #111111;
    --overlay: rgba(20, 20, 20, 0.38);
    --text-light: #ffffff;
  }
  * { margin: 0; padding: 0; box-sizing: border-box; }
  html, body {
    width: 1200px;
    height: 1200px;
    overflow: hidden;
    background: var(--page-bg);
    font-family: "Nunito", sans-serif;
  }
  .ad {
    position: absolute;
    left: 50px;
    top: 230px;
    width: 1100px;
    height: 739px;
    background: var(--card-white);
    overflow: hidden;
  }
  .ad__photo {
    position: absolute;
    left: 0; top: 0;
    width: 1100px;
    height: 542px;
    background:
      radial-gradient(ellipse at 28% 45%, rgba(150,140,70,0.55), transparent 60%),
      linear-gradient(100deg, #7d7440 0%, #5e5a32 38%, #3e3828 62%, #2a2330 100%);
  }
  .ad__message {
    position: absolute;
    left: 497px;
    top: 288px;
    width: 564px;
    height: 254px;
    background: var(--overlay);
  }
  .ad__headline {
    position: absolute;
    left: 493px;
    top: 186px;
    font-weight: 800;
    font-size: 86px;
    line-height: 1;
    color: var(--lime);
    letter-spacing: -0.5px;
  }
  .ad__copy {
    position: absolute;
    left: 533px;
    top: 298px;
    color: var(--text-light);
    font-size: 37px;
    line-height: 47px;
    font-weight: 400;
  }
  .ad__copy p + p { margin-top: 47px; }
  .ad__rule {
    position: absolute;
    left: 0; top: 542px;
    width: 1100px;
    height: 8px;
    background: var(--teal);
  }
  .brand {
    position: absolute;
    left: 36px;
    top: 622px;
    display: flex;
    align-items: center;
    gap: 12px;
  }
  .brand__dot {
    width: 38px; height: 38px;
    border-radius: 50%;
    background: var(--teal);
  }
  .brand__name {
    font-size: 22px;
    font-weight: 400;
    color: var(--brand-blue);
  }
  .address {
    position: absolute;
    left: 365px;
    top: 597px;
    font-size: 24px;
    line-height: 30.5px;
    color: var(--ink);
    font-style: normal;
  }
  .contact {
    position: absolute;
    left: 703px;
    top: 597px;
    color: var(--ink);
  }
  .contact__phone {
    font-size: 34px;
    font-weight: 800;
    line-height: 42px;
  }
  .contact__line {
    font-size: 24px;
    line-height: 31px;
    padding-left: 13px;
  }
</style>
</head>
<body>
  <section class="ad">
    <div class="ad__photo" role="img" aria-label="Photo of a young boy and his father planting a sapling together in soil"></div>
    <div class="ad__message"></div>
    <h1 class="ad__headline">Children</h1>
    <div class="ad__copy">
      <p>They are the most<br>important thing in your life.</p>
      <p>Let us help you<br>protect what you love.</p>
    </div>
    <div class="ad__rule"></div>

    <div class="brand">
      <span class="brand__dot"></span>
      <span class="brand__name">Briar Hollow Family Law</span>
    </div>

    <address class="address">
      1420 Marlowe Street<br>
      Suite 210<br>
      Greenfield, NC 28471
    </address>

    <div class="contact">
      <div class="contact__phone">+1 (910) 555-0172</div>
      <div class="contact__line">nora@briarhollowfamilylaw.com</div>
      <div class="contact__line">www.briarhollowfamilylaw.com</div>
    </div>
  </section>
</body>
</html>
```